Healthy Snack Bar Wrapper Design

We are passionate about delivering healthy and tasty treats that are Raw, Organic, Preservative Free, Gluten Free, have No Added Sugar and No Additives!
In this project we are looking for a design for a new healthy food product to be launched soon in Australia. The packaging will be a bar wrapper made from foil that will be hot sealed, with a front and a back.
The snack is a raw, organic and healthy treat made predominantly with nuts, and will come in 3 initial flavours:
- Velvet Harbor (Sour Cherry and Choc)
- Plum Fizzaroo (Banana, Apricot and Blueberry)
- Sunmelodia (Pineapple, Passionfruit and Kiwi)
The product name is MunchWell, which does not currently have a logo. We are happy to have this as a simple written component of the initial design at the top of the packaging, perhaps within an circle, square or oval.
The typeface used for the names and the main ingredients should be fun.
The overall design should be very simple and make use of minimal colours. Our preferences are to have a plain colour for the background, such as light organic brown or white, with an eye catching colour that can be used to define the flavour, but should not be too vibrant.
We do not want to have an 3 dimensional images or objects. Nor do we want to have product images and any imagery should be only to give the impression of the flavours within rather than an image of the flavour. Finally, we do not want to have gradients included in the design.
The final design should communicate healthy, tasty and fun!
Examples of inspiration designs are attached in the files.
Main Information:
- The front should comprise of the following information:
-- MunchWell
-- Flavour name (such as Velvet Harbor)
-- Main Ingredients (Sour Cherry and Choc) (This is optional)
-- Portion size (60g)
-- Message (This is optional)
--- 0% Additives
--- 60% Nuts
--- 100% Natural
- The back needs to have space for the following information:
-- Nutritional Information
-- Barcode
-- Ingredients
-- Contact information
- Wrapper Dimensions
-- Width: 14cm
-- Height: 15cm
- Bar Dimensions
-- Width: 3cm
-- Height: 10cm
-- Depth: 2.5cm
Target Market(s)
People who want to have a healthy tasty treat
Colors
Designer to choose colors to be used in the design.
Requirements
Must have
- Main Information:
- - The front should comprise of the following information:
- -- MunchWell
- -- Flavour name (such as Velvet Harbor)
- -- Main Ingredients (Sour Cherry and Choc) (This is optional)
- -- Portion size (60g)
- -- Message (This is optional)
- --- 0% Additives
- --- 60% Nuts
- --- 100% Natural
- - The back needs to have space for the following information:
- -- Nutritional Information
- -- Barcode
- -- Ingredients
- -- Contact information
- - Wrapper Dimensions
- -- Width: 14cm
- -- Height: 15cm
- - Bar Dimensions
- -- Width: 3cm
- -- Height: 10cm
- -- Depth: 2.5cm
Should not have
- We do not want to have an 3 dimensional images or objects. Nor do we want to have product images and any imagery should be only to give the impression of the flavours within rather than an image of the flavour. Finally, we do not want to have gradients included in the design.

```html
<!DOCTYPE html>
<html lang="en">
<head>
<meta charset="utf-8">
<title>MunchWell bar wrappers</title>
<link rel="stylesheet" href="https://fonts.googleapis.com/css2?family=Bebas+Neue&display=swap">
<style>
  :root {
    --kraft: #c4a86f;
    --kraft-dark: #b0945c;
    --paper: #ffffff;
    --ink: #2b2b2b;
    --cherry: #8c1628;
    --cherry-dark: #761020;
    --banana: #d6c91f;
    --banana-dark: #c2b512;
    --kiwi: #20a84a;
    --kiwi-dark: #14903b;
  }
  * { box-sizing: border-box; margin: 0; padding: 0; }
  html, body {
    width: 1200px;
    height: 884px;
    overflow: hidden;
    background: var(--paper);
  }
  .lineup { position: relative; width: 1200px; height: 884px; }

  .wrapper {
    position: absolute;
    top: 156px;
    width: 192px;
    height: 522px;
    background: var(--kraft);
    overflow: hidden;
    font-family: "Bebas Neue", sans-serif;
  }
  .wrapper--cherry { left: 300px; --flavour: var(--cherry); --flavour-dark: var(--cherry-dark); }
  .wrapper--banana { left: 520px; --flavour: var(--banana); --flavour-dark: var(--banana-dark); }
  .wrapper--kiwi   { left: 740px; --flavour: var(--kiwi);   --flavour-dark: var(--kiwi-dark); }

  .seal {
    position: absolute;
    left: 0; right: 0;
    height: 26px;
    background: repeating-linear-gradient(90deg, var(--seal) 0 4px, var(--seal-line) 4px 5px);
  }
  .seal--top { top: 0; --seal: var(--kraft); --seal-line: var(--kraft-dark); }
  .seal--bottom { bottom: 0; --seal: var(--flavour); --seal-line: var(--flavour-dark); }

  .brand {
    position: absolute;
    top: 62px;
    left: 0; right: 0;
    display: flex;
    align-items: center;
    justify-content: center;
    gap: 8px;
    font-size: 26px;
    line-height: 32px;
    letter-spacing: 1px;
    color: var(--paper);
  }
  .brand-dot {
    width: 12px;
    height: 12px;
    border-radius: 50%;
    background: var(--paper);
  }

  .flavour-name {
    position: absolute;
    top: 124px;
    left: 0; right: 0;
    text-align: center;
    font-weight: 400;
    font-size: 58px;
    line-height: 50px;
    letter-spacing: 1px;
    color: var(--paper);
  }
  .flavour-name--long { font-size: 52px; }

  .ingredients-band {
    position: absolute;
    top: 224px;
    left: 0; right: 0;
    height: 110px;
    background: var(--paper);
    clip-path: polygon(0 30%, 10% 24%, 22% 20%, 34% 16%, 46% 14%, 58% 10%, 70% 8%, 82% 4%, 92% 2%, 100% 0,
                       100% 76%, 88% 80%, 76% 84%, 64% 86%, 52% 90%, 40% 92%, 28% 95%, 16% 98%, 0 100%);
    display: flex;
    align-items: center;
    justify-content: center;
    text-align: center;
    font-size: 18px;
    line-height: 18px;
    letter-spacing: 0.5px;
    color: var(--ink);
  }

  .flavour-panel {
    position: absolute;
    top: 318px;
    left: 0; right: 0; bottom: 0;
    background: var(--flavour);
    clip-path: polygon(0 22px, 100% 0, 100% 100%, 0 100%);
  }
  .claims {
    position: absolute;
    top: 50px;
    left: 18px;
    list-style: none;
    font-size: 27px;
    line-height: 36px;
    letter-spacing: 1px;
    color: var(--paper);
    transform: rotate(-4deg);
    transform-origin: left top;
  }
  .claims u { text-decoration-thickness: 2px; text-underline-offset: 3px; }
  .portion {
    position: absolute;
    top: 152px;
    left: 0; right: 0;
    text-align: center;
    font-size: 14px;
    color: var(--paper);
  }
</style>
</head>
<body>
<main class="lineup">

  <article class="wrapper wrapper--cherry">
    <div class="seal seal--top"></div>
    <div class="brand"><span class="brand-dot"></span>MunchWell</div>
    <h2 class="flavour-name">Velvet<br>Harbor</h2>
    <p class="ingredients-band">Sour cherry<br>and choc</p>
    <div class="flavour-panel">
      <ul class="claims">
        <li>0% <u>Additives</u></li>
        <li>60% Nuts</li>
        <li>100% Natural</li>
      </ul>
      <p class="portion">60G</p>
      <div class="seal seal--bottom"></div>
    </div>
  </article>

  <article class="wrapper wrapper--banana">
    <div class="seal seal--top"></div>
    <div class="brand"><span class="brand-dot"></span>MunchWell</div>
    <h2 class="flavour-name flavour-name--long">Plum<br>Fizzaroo</h2>
    <p class="ingredients-band">Banana<br>apricot and<br>blueberry</p>
    <div class="flavour-panel">
      <ul class="claims">
        <li>0% <u>Additives</u></li>
        <li>60% Nuts</li>
        <li>100% Natural</li>
      </ul>
      <p class="portion">60G</p>
      <div class="seal seal--bottom"></div>
    </div>
  </article>

  <article class="wrapper wrapper--kiwi">
    <div class="seal seal--top"></div>
    <div class="brand"><span class="brand-dot"></span>MunchWell</div>
    <h2 class="flavour-name flavour-name--long">Sun<br>Melodia</h2>
    <p class="ingredients-band">Pineapple<br>passionfruit<br>and kiwi</p>
    <div class="flavour-panel">
      <ul class="claims">
        <li>0% <u>Additives</u></li>
        <li>60% Nuts</li>
        <li>100% Natural</li>
      </ul>
      <p class="portion">60G</p>
      <div class="seal seal--bottom"></div>
    </div>
  </article>

</main>
</body>
</html>
```